Sleek Design For Personal Brand Wordpress Website !!

*WORDPRESS WEBSITE*

Need a sleek and easy to navigate Wordpress website.

It will act as the hub for my personal brand.

Which means it will showcase all my social media outlets, host my most recent content like Vidstream videos and podcasts...

It will also be the go to place to find all my digital products and services that I offer.

i want it to be super sleek and simple but also give a personal touch of my who I really am. You can get a good idea of who I am my checking out my Snapfeed (@karel.dumonte)

Use these websites for ideas: www.brevanhollis.example and www.dorianfelkowitz.example

Target Market(s)

Young Entrepreneurs

Industry/Entity Type

Education

Logo Text

Karel Dumonte

Number of Pages Required

4 page

Font styles to use
Sans Serif

Colors
ffffff
0392cd
ec1f27

Requirements
Must have
• Social Media buttons on the home page...
• Video (also a slider) right at the top of the home page...
• Email Optin...
• Multiple pages...

```html
<!DOCTYPE html>
<html lang="en">
<head>
<meta charset="utf-8">
<title>Karel Dumonte</title>
<link href="https://fonts.googleapis.com/css2?family=Audiowide&family=Open+Sans:wght@400;600;700&family=Roboto+Condensed:wght@700&display=swap" rel="stylesheet">
<style>
:root{
  --red:#ec1f27;
  --blue:#0392cd;
  --white:#ffffff;
  --ink:#1b1b1b;
  --grey:#777777;
  --light:#f3f2ef;
  --dark:#141414;
  --footer:#333333;
  --field:#555555;
  --tile-brown:#5a4214;
  --tile-blue:#2a5fc4;
  --tile-cyan:#1ab7e0;
}
*{margin:0;padding:0;box-sizing:border-box}
html,body{width:1200px;height:2639px;overflow:hidden;background:var(--white)}
body{font-family:"Open Sans",sans-serif;color:var(--ink);position:relative}
.display{font-family:"Audiowide",sans-serif;font-style:italic;text-transform:uppercase;letter-spacing:2px}

/* header */
.site-header{position:absolute;left:0;top:0;width:1200px;height:74px;background:var(--white)}
.brand{position:absolute;left:184px;top:14px;display:flex;align-items:center;gap:10px}
.brand-dot{width:44px;height:44px;border-radius:50%;background:#e8e8e8}
.brand-name{font-weight:700;font-size:22px;color:var(--red)}
.main-nav{position:absolute;left:513px;top:28px;display:flex;align-items:center;font-size:11px;font-weight:600;text-transform:uppercase;color:#444}
.main-nav a{color:inherit;text-decoration:none;margin-right:50px}
.main-nav a.current{color:var(--ink);font-weight:700}
.main-nav a:last-child{margin-right:0}

/* hero */
.hero{position:absolute;left:0;top:74px;width:1200px;height:519px;overflow:hidden}
.hero-bg{position:absolute;inset:0;background:linear-gradient(90deg,#ecebe8 0%,#e0dfdb 45%,#bdbcb8 58%,#c9c8c4 64%,#8f948c 66%,#a9aea6 82%,#7d827a 100%)}
.hero-figure{position:absolute;left:560px;top:0;width:218px;height:519px;background:linear-gradient(180deg,#cfcfcd 0%,#8a8a88 55%,#5a5a58 100%);opacity:.55}
.hero-intro{position:absolute;left:160px;top:116px;font-size:12px;color:#6a6a6a}
.hero-title{position:absolute;left:158px;top:174px;font-size:43px;line-height:58px;color:#4a4a4a}
.hero-link{position:absolute;left:160px;top:310px;font-size:12px;font-weight:700;color:var(--red);text-transform:uppercase;padding-bottom:6px;border-bottom:2px solid var(--red)}
.slider-arrow{position:absolute;top:244px;width:32px;height:32px;background:#3a3a3a;display:flex;align-items:center;justify-content:center}
.slider-arrow.prev{left:56px}
.slider-arrow.next{left:1120px;background:#2a2a2a}
.play-button{position:absolute;left:960px;top:224px;width:72px;height:72px;border-radius:50%;border:3px solid rgba(255,255,255,.85);background:rgba(0,0,0,.25);display:flex;align-items:center;justify-content:center}

/* intro band */
.intro-band{position:absolute;left:0;top:593px;width:1200px;height:185px;background:var(--light);text-align:center}
.intro-band h2{position:absolute;left:0;right:0;top:40px;font-size:24px;color:var(--red)}
.intro-rule{position:absolute;left:533px;top:82px;width:134px;height:3px;background:var(--red)}
.intro-band p{position:absolute;left:0;right:0;top:105px;font-size:12px;line-height:19px;color:#666}

/* about */
.about{position:absolute;left:0;top:778px;width:1200px;height:507px;background:var(--white)}
.portrait{position:absolute;left:161px;top:57px;width:300px;height:300px;border-radius:50%;border:6px solid #e4e4e4;background:linear-gradient(160deg,#9bb0bf 0%,#5f6e78 45%,#e9e9e9 100%)}
.welcome{position:absolute;left:312px;top:207px;width:232px;height:232px;border-radius:50%;background:var(--white);border:1px solid #e2e2e2;text-align:center;padding-top:54px}
.welcome h3{font-family:"Roboto Condensed",sans-serif;font-size:26px;color:var(--ink)}
.welcome p{font-size:11.5px;line-height:18px;color:#555;margin:14px 28px 0}
.about-copy{position:absolute;left:580px;top:105px;width:460px}
.about-copy h2{font-size:26px;color:var(--ink)}
.about-lead{font-size:11.5px;line-height:17px;color:var(--red);text-transform:uppercase;margin-top:12px}
.about-copy p.body{font-size:12px;line-height:20px;color:#777;margin-top:14px}

/* learn */
.learn{position:absolute;left:0;top:1285px;width:1200px;height:410px;overflow:hidden}
.learn-bg{position:absolute;inset:0;background:linear-gradient(90deg,#121212 0%,#181818 45%,#3b3d3a 62%,#5b615b 80%,#6f7872 100%)}
.learn-title{position:absolute;left:160px;top:62px;font-size:30px;line-height:42px;color:var(--white)}
.learn-sub{position:absolute;left:160px;top:150px;font-size:10px;font-weight:700;font-style:italic;color:var(--red)}
.learn-text{position:absolute;left:160px;top:172px;width:480px;font-size:11.5px;line-height:20px;color:#dcdcdc}
.learn-btn{position:absolute;left:160px;top:246px;width:112px;height:40px;border:2px solid var(--white);border-radius:3px;color:var(--white);font-size:11px;font-weight:700;display:flex;align-items:center;justify-content:center}
.quote-bar{position:absolute;left:0;top:334px;width:1200px;height:76px;background:rgba(0,0,0,.8)}
.quote-icon{position:absolute;left:162px;top:20px;width:34px;height:34px;border-radius:50%;background:var(--red);display:flex;align-items:center;justify-content:center}
.quote-text{position:absolute;left:216px;top:27px;font-size:15px;font-style:italic;color:var(--white)}
.quote-author{position:absolute;left:739px;top:29px;font-size:11.5px;color:#cfcfcd}
.quote-author b{color:var(--red)}

/* events */
.events{position:absolute;left:0;top:1695px;width:1200px;height:183px;background:var(--white)}
.events-card{position:absolute;left:160px;top:49px;width:880px;height:88px;background:var(--red);color:var(--white)}
.events-card h2{position:absolute;left:24px;top:30px;font-size:23px;letter-spacing:1px}
.events-card p{position:absolute;left:334px;top:16px;font-size:11px;line-height:19px;white-space:nowrap}
.events-card .date{left:697px;top:34px;font-size:12px}

/* social */
.social{position:absolute;left:0;top:1878px;width:1200px;height:375px;background:var(--light)}
.social h2{position:absolute;left:0;right:0;top:64px;text-align:center;font-size:30px;color:var(--ink)}
.tile{position:absolute;top:144px;width:203px;height:160px;border:3px solid #dcdcdc;color:var(--white);text-align:center}
.tile .network{display:block;margin-top:20px;font-weight:700;font-size:13px}
.tile p{font-family:"Audiowide",sans-serif;font-style:italic;text-transform:uppercase;font-size:10px;line-height:18px;margin:16px 14px 0;letter-spacing:.5px}
.tile.snap{left:160px;background:var(--tile-brown)}
.tile.vid{left:385px;background:var(--red)}
.tile.friend{left:611px;background:var(--tile-blue)}
.tile.chirp{left:834px;background:var(--tile-cyan)}

/* subscribe */
.subscribe{position:absolute;left:0;top:2253px;width:1200px;height:58px;background:var(--red)}
.subscribe h2{position:absolute;left:158px;top:14px;font-size:21px;color:var(--white);text-transform:none}
.subscribe .field{position:absolute;left:412px;top:12px;width:523px;height:36px;background:var(--white);font-size:11px;color:#999;padding:11px 12px}
.subscribe .submit{position:absolute;left:944px;top:12px;width:96px;height:36px;border:2px solid var(--white);color:var(--white);font-size:13px;display:flex;align-items:center;justify-content:center}

/* footer */
.site-footer{position:absolute;left:0;top:2311px;width:1200px;height:328px;background:var(--footer);color:#bdbdbd}
.site-footer h4{position:absolute;top:26px;font-family:"Audiowide",sans-serif;font-style:italic;font-weight:400;font-size:14px;color:var(--white);letter-spacing:1px}
.f-input{position:absolute;background:var(--field);font-size:10px;color:#ddd;padding:10px 8px}
.f-send{position:absolute;left:160px;top:197px;width:104px;height:38px;background:var(--red);color:var(--white);font-family:"Audiowide",sans-serif;font-style:italic;font-size:13px;display:flex;align-items:center;justify-content:center}
.f-links{position:absolute;top:70px;list-style:none;font-size:11px;line-height:24px;color:#aaa}
.f-address{position:absolute;left:858px;top:66px;width:190px;font-size:11px;color:#aaa}
.f-address div{position:relative;padding-left:30px;margin-bottom:22px;line-height:16px}
.f-address svg{position:absolute;left:0;top:1px}
.f-rule{position:absolute;left:160px;top:276px;width:880px;height:1px;background:#4a4a4a}
.copyright{position:absolute;left:160px;top:298px;font-size:11px;color:#aaa}
.f-social{position:absolute;left:950px;top:290px;display:flex;gap:8px}
.f-social span{width:26px;height:26px;border-radius:50%;border:1.5px solid #bbb}
</style>
</head>
<body>

<header class="site-header">
  <div class="brand"><span class="brand-dot"></span><span class="brand-name">Karel Dumonte</span></div>
  <nav class="main-nav">
    <a href="#"><svg width="18" height="16" viewBox="0 0 18 16"><path d="M9 1 L17 8 H14.5 V15 H10.5 V10.5 H7.5 V15 H3.5 V8 H1 Z" fill="#ec1f27"/></svg></a>
    <a href="#" class="current">About</a>
    <a href="#">Event</a>
    <a href="#">Podcast</a>
    <a href="#">Hire Me To Speak</a>
    <a href="#">Blog</a>
    <a href="#">Contact</a>
  </nav>
</header>

<section class="hero">
  <div class="hero-bg" role="img" aria-label="Video slider: photo of the host standing in a light jacket beside a private jet on a runway"></div>
  <div class="hero-figure" role="img" aria-label="Host portrait in black and white"></div>
  <p class="hero-intro">Hi, I'm Karel Dumonte.Vidstream videos and podcasts.</p>
  <h1 class="hero-title display">Free Training<br>Reveals:</h1>
  <a class="hero-link">Show me exactly how you did it</a>
  <span class="slider-arrow prev"><svg width="10" height="12" viewBox="0 0 10 12"><path d="M7 1 L2 6 L7 11" stroke="#fff" stroke-width="2" fill="none"/></svg></span>
  <span class="slider-arrow next"><svg width="10" height="12" viewBox="0 0 10 12"><path d="M3 1 L8 6 L3 11" stroke="#fff" stroke-width="2" fill="none"/></svg></span>
  <span class="play-button"><svg width="22" height="26" viewBox="0 0 22 26"><path d="M3 2 L20 13 L3 24 Z" fill="#fff"/></svg></span>
</section>

<section class="intro-band">
  <h2 class="display">Free Training Reveals:</h2>
  <span class="intro-rule"></span>
  <p>We Will Teach You Step-By-Step How We Went From $0 to $224K A Month On Storevane!<br>We Will Take You By The Hand To Show You Exactly How We Did It!</p>
</section>

<section class="about">
  <div class="portrait" role="img" aria-label="Circular photo of the host in sunglasses and a white jacket"></div>
  <div class="welcome">
    <h3>Welcome,</h3>
    <p>Lorem ipsum dolor sit amet, consec adipiscing elit, sed do eiusmod tempor incididunt ut labore et dolore magna aliqua.</p>
  </div>
  <div class="about-copy">
    <h2 class="display">Karel Dumonte</h2>
    <p class="about-lead">Lorem ipsum dolor sit amet, consectetur adipiscing elit, sed do eiusmod tempor incididunt ut labore et dolore.</p>
    <p class="body">Lorem ipsum dolor sit amet, consectetur adipiscing elit, sed do eiusmod tempor incididunt ut labore et dolore magna aliqua. Ut enim ad minim veniam, quis nostrud exercitation ullamco laboris nisi ut aliquip ex ea commodo consequat.</p>
    <p class="body">Duis aute irure dolor in reprehenderit in voluptate velit esse cillum dolore eu fugiat nulla pariatur. Excepteur sint occaecat cupidatat non proident, sunt in culpa qui officia deserunt mollit anim id est laborum.</p>
  </div>
</section>

<section class="learn">
  <div class="learn-bg" role="img" aria-label="Photo of the host standing in a bright office lobby"></div>
  <h2 class="learn-title display">What you will learn<br>on this free training:</h2>
  <p class="learn-sub">Show Me Exactly How You Did It</p>
  <p class="learn-text">HOW YOU CREATE A STOREVANE STORE THAT CONVERTS Building an eCommerce store is simple but building a store that actually makes people want to buy is more important!</p>
  <a class="learn-btn">LEARN MORE</a>
  <div class="quote-bar">
    <span class="quote-icon"><svg width="16" height="12" viewBox="0 0 16 12"><path d="M1 12 V6 Q1 1 6 0 V2 Q3 3 3 6 H6 V12 Z M9 12 V6 Q9 1 14 0 V2 Q11 3 11 6 H14 V12 Z" fill="#fff"/></svg></span>
    <p class="quote-text">Duis aute irure dolor in reprehenderit in voluptate velit esse cillum</p>
    <p class="quote-author"><b>Linus Ardwell,</b>&nbsp; Harlow Peak Homes | Millbrook, OR</p>
  </div>
</section>

<section class="events">
  <div class="events-card">
    <h2 class="display">Upcoming Events</h2>
    <p>Lorem ipsum dolor sit amet, consectetur adipiscing elit, sed<br>do eiusmod tempor incididunt ut labore et dolore magna aliqua.<br>Ut enim ad minim veniam, quis nostrud exercitation.</p>
    <p class="date">Dec 31-12, 2017 ~ Coral Bay,</p>
  </div>
</section>

<section class="social">
  <h2 class="display">Stay in touch with me.</h2>
  <div class="tile snap"><span class="network">Snapfeed</span><p>My favorite place. Quotes, stories &amp; your chance to win the #minutecrew</p></div>
  <div class="tile vid"><span class="network">Vidstream</span><p>Documenting my life through #dailykd &amp; #askkarel ;)</p></div>
  <div class="tile friend"><span class="network">Friendhub</span><p>My biggest platform. Join the Dumonte Nation &amp; stay up to date on everything I do.</p></div>
  <div class="tile chirp"><span class="network">Chirpline</span><p>The most direct &amp; personal way to reach me for 1-1 conversations.</p></div>
</section>

<section class="subscribe">
  <h2 class="display">Subscribe Here :</h2>
  <div class="field">Enter Your Email Here...</div>
  <div class="submit display">Submit</div>
</section>

<footer class="site-footer">
  <h4 style="left:160px">CONTACT US</h4>
  <div class="f-input" style="left:160px;top:56px;width:170px;height:40px">Name :</div>
  <div class="f-input" style="left:336px;top:56px;width:172px;height:40px">Email :</div>
  <div class="f-input" style="left:160px;top:102px;width:348px;height:86px">Message :</div>
  <div class="f-send">SUBMIT</div>

  <h4 style="left:580px">NAVIGATION</h4>
  <ul class="f-links" style="left:581px"><li>Home</li><li>About Us</li><li>Events</li><li>Podcaste</li><li>Hire Me To Speak</li></ul>
  <ul class="f-links" style="left:686px"><li>Terms &amp; Condition</li><li>Privacy Policy</li><li>Help</li></ul>

  <h4 style="left:858px">ADDRESSS</h4>
  <div class="f-address">
    <div><svg width="12" height="16" viewBox="0 0 12 16"><path d="M6 0 C2.7 0 0 2.6 0 5.8 C0 10 6 16 6 16 C6 16 12 10 12 5.8 C12 2.6 9.3 0 6 0 Z M6 8 A2.2 2.2 0 1 1 6 3.6 A2.2 2.2 0 1 1 6 8 Z" fill="#bbb"/></svg>Aoluptas sit aspernatur aut odit fugit, sed quias consequuntur</div>
    <div><svg width="16" height="12" viewBox="0 0 16 12"><rect x="0.5" y="0.5" width="15" height="11" fill="none" stroke="#bbb"/><path d="M0.5 0.5 L8 7 L15.5 0.5" fill="none" stroke="#bbb"/></svg>info@kareldumonte.example</div>
    <div><svg width="16" height="14" viewBox="0 0 16 14"><path d="M1 4 Q8 -1 15 4 L13 6 L11 4.5 V3 H5 V4.5 L3 6 Z M3 7 H13 L14 13 H2 Z" fill="#bbb"/></svg>012 345 6789</div>
  </div>

  <div class="f-rule"></div>
  <p class="copyright">Copyright © 2017 Karel Dumonte, All Rights Reserved &nbsp; / &nbsp; Privacy Policy</p>
  <div class="f-social"><span></span><span></span><span></span></div>
</footer>

</body>
</html>
```